Looking for a professional, clean and crisp business card

I am in the underground utilities industry and am just looking for a really impressive business card. I would like our card to be white with our symbol crisp and clear with it protruding. I also have a business partner that will require his name and info on the card once the design is set. I would like to have our website info on the card which is;
http://harbortrenchco.example/

Contact Information for Business Card

Website, contact name, number and email

```html
<!DOCTYPE html>
<html lang="en">
<head>
<meta charset="utf-8">
<title>Harbor Trench Co — Business Cards</title>
<link href="https://fonts.googleapis.com/css2?family=Lato:wght@400;700;900&display=swap" rel="stylesheet">
<style>
  :root {
    --backdrop: #2e302f;
    --card-white: #ffffff;
    --card-black: #141414;
    --ink: #1b1b1b;
    --muted: #5a5a5a;
    --accent: #3b73b9;
    --pattern-light: #2a2a2a;
  }
  * { margin: 0; padding: 0; box-sizing: border-box; }
  html, body {
    width: 1200px;
    height: 3316px;
    overflow: hidden;
    background: var(--backdrop);
    font-family: "Lato", Arial, sans-serif;
  }
  .sheet {
    width: 1200px;
    height: 3316px;
    display: flex;
    flex-direction: column;
    justify-content: space-around;
    align-items: center;
  }
  .card-pair {
    display: flex;
    gap: 14px;
    align-items: flex-start;
  }
  .card {
    width: 340px;
    height: 580px;
    border-radius: 22px;
    overflow: hidden;
    position: relative;
  }
  .card-front {
    background: var(--card-white);
    display: flex;
    flex-direction: column;
    align-items: center;
    padding: 48px 20px 0;
    color: var(--ink);
  }
  .brand-mark {
    display: flex;
    flex-direction: column;
    align-items: center;
    gap: 16px;
    margin-bottom: 52px;
  }
  .brand-dot {
    width: 150px;
    height: 150px;
    border-radius: 50%;
    background: var(--ink);
  }
  .brand-name {
    font-weight: 900;
    font-size: 24px;
    letter-spacing: 1px;
    text-transform: uppercase;
    white-space: nowrap;
    color: var(--ink);
  }
  .person-name {
    font-weight: 900;
    font-size: 27px;
    color: var(--ink);
  }
  .person-title {
    font-size: 15px;
    color: var(--muted);
    margin-top: 2px;
  }
  .badge-row {
    display: flex;
    align-items: center;
    gap: 8px;
    margin: 16px 0 16px;
  }
  .badge-row::before, .badge-row::after {
    content: "";
    width: 50px;
    height: 2px;
    background: var(--accent);
  }
  .badge-row span {
    width: 16px;
    height: 16px;
    border-radius: 50%;
    background: var(--accent);
  }
  .contact-list {
    list-style: none;
    text-align: center;
    font-size: 16px;
    line-height: 1.8;
    color: var(--muted);
  }
  .card-back {
    background: var(--card-black);
    margin-top: 40px;
  }
  .back-texture {
    position: absolute;
    inset: 0;
    background: linear-gradient(160deg, var(--pattern-light) 0%, var(--card-black) 70%);
  }
  .back-brand {
    position: absolute;
    left: 0;
    right: 0;
    bottom: 80px;
    text-align: center;
    color: var(--card-white);
    font-weight: 900;
    font-size: 26px;
    letter-spacing: 2px;
    text-transform: uppercase;
    white-space: nowrap;
  }
</style>
</head>
<body>
<main class="sheet">

  <section class="card-pair">
    <article class="card card-front">
      <div class="brand-mark"><span class="brand-dot"></span><span class="brand-name">Harbor Trench Co</span></div>
      <h2 class="person-name">Dale Marrow</h2>
      <p class="person-title">Owner</p>
      <div class="badge-row"><span></span><span></span><span></span></div>
      <ul class="contact-list">
        <li>555-014-2290</li>
        <li>dale@harbortrenchco.example</li>
        <li>www.harbortrenchco.example</li>
      </ul>
    </article>
    <article class="card card-back">
      <div class="back-texture" role="img" aria-label="Faint repeated company name pattern across the dark card back"></div>
      <p class="back-brand">Harbor Trench Co</p>
    </article>
  </section>

  <section class="card-pair">
    <article class="card card-front">
      <div class="brand-mark"><span class="brand-dot"></span><span class="brand-name">Harbor Trench Co</span></div>
      <h2 class="person-name">Ross Keller</h2>
      <p class="person-title">Owner</p>
      <div class="badge-row"><span></span><span></span><span></span></div>
      <ul class="contact-list">
        <li>555-014-2291</li>
        <li>ross@harbortrenchco.example</li>
        <li>www.harbortrenchco.example</li>
      </ul>
    </article>
    <article class="card card-back">
      <div class="back-texture" role="img" aria-label="Faint repeated company name pattern across the dark card back"></div>
      <p class="back-brand">Harbor Trench Co</p>
    </article>
  </section>

  <section class="card-pair">
    <article class="card card-front">
      <div class="brand-mark"><span class="brand-dot"></span><span class="brand-name">Harbor Trench Co</span></div>
      <h2 class="person-name">Glen Oakes</h2>
      <p class="person-title">Estimator</p>
      <div class="badge-row"><span></span><span></span><span></span></div>
      <ul class="contact-list">
        <li>555-014-2292</li>
        <li>glen@harbortrenchco.example</li>
        <li>www.harbortrenchco.example</li>
      </ul>
    </article>
    <article class="card card-back">
      <div class="back-texture" role="img" aria-label="Faint repeated company name pattern across the dark card back"></div>
      <p class="back-brand">Harbor Trench Co</p>
    </article>
  </section>

</main>
</body>
</html>
```